Business Card Design

Business Card for professional consulting firm working with large financial institutions.

Target Market(s)

Executive buyers

Industry/Entity Type

Banking

Contact Information for Business Card

Mild creativity wanted. Not boring, but do elaborate artwork.

Font styles to use
Serif
Sans Serif

Colors

Designer to choose colors to be used in the design.

Requirements
Must have
• Standard business card features - company name, individual name, telephone, website, email, locations.
Nice to have
• Two colors
Should not have
• too many colors, fancy printing, cartoons.

```html
<!DOCTYPE html>
<html lang="en">
<head>
<meta charset="utf-8">
<title>Veldmark Business Card</title>
<link href="https://fonts.googleapis.com/css2?family=Lato:wght@400;700&display=swap" rel="stylesheet">
<style>
  :root {
    --page: #161616;
    --card: #1c1c1d;
    --silver: #e4e4e4;
    --muted: #8c8c8c;
    --text: #cfcfcf;
    --accent: #1f3a9a;
    --rule: #bdbdbd;
  }
  * { margin: 0; padding: 0; box-sizing: border-box; }
  html, body { width: 1200px; height: 900px; overflow: hidden; background: var(--page); }
  body { position: relative; font-family: "Lato", sans-serif; }

  .card {
    position: absolute;
    width: 540px;
    height: 310px;
    background: var(--card);
    border-radius: 22px;
    box-shadow: 0 18px 40px rgba(0,0,0,.55);
  }
  .card--front { left: 110px; top: 110px; }
  .card--back { left: 550px; top: 480px; }

  .brand {
    position: absolute;
    font-weight: 400;
    letter-spacing: .5px;
    white-space: nowrap;
  }
  .card--front .brand {
    left: 0; right: 0; top: 128px;
    text-align: center;
    font-size: 40px;
    color: var(--silver);
  }
  .card--back .brand {
    right: 34px; top: 36px;
    font-size: 30px;
    color: var(--accent);
  }

  .rule {
    position: absolute;
    left: 250px; right: 30px; top: 120px;
    height: 1px;
    background: var(--rule);
  }

  .person { position: absolute; left: 34px; top: 132px; }
  .person__name { font-size: 22px; font-weight: 700; color: var(--silver); letter-spacing: .5px; }
  .person__role { font-size: 15px; color: var(--muted); margin-top: 2px; }

  .contacts {
    position: absolute;
    right: 30px; top: 136px;
    list-style: none;
    font-size: 15px;
    color: var(--text);
    text-align: right;
    line-height: 22px;
  }
  .contacts li { display: flex; justify-content: flex-end; align-items: center; gap: 8px; }
  .contacts svg { width: 12px; height: 12px; fill: var(--silver); }

  .address {
    position: absolute;
    left: 34px; bottom: 34px;
    font-size: 17px;
    color: var(--text);
    line-height: 22px;
    font-style: normal;
  }
</style>
</head>
<body>
  <section class="card card--front">
    <div class="brand">veldmark</div>
  </section>

  <section class="card card--back">
    <div class="brand">veldmark</div>
    <div class="rule"></div>

    <div class="person">
      <div class="person__name">DANIEL HARTLEY</div>
      <div class="person__role">Managing Director</div>
    </div>

    <ul class="contacts">
      <li>044-123 456 789
        <svg viewBox="0 0 12 12" aria-hidden="true"><path d="M1 4 Q6 0 11 4 L9 5 L8 3.5 Q6 3 4 3.5 L3 5 Z M3 6 H9 L10 11 H2 Z"/></svg>
      </li>
      <li>info@webname.com
        <svg viewBox="0 0 12 12" aria-hidden="true"><rect x="0" y="2" width="12" height="8" rx="1"/><path d="M0.5 2.5 L6 7 L11.5 2.5" stroke="#1c1c1d" stroke-width="1" fill="none"/></svg>
      </li>
      <li>www.websitename.com
        <svg viewBox="0 0 12 12" aria-hidden="true"><circle cx="6" cy="6" r="6"/><path d="M1 6 H11 M6 0.5 Q3 6 6 11.5 M6 0.5 Q9 6 6 11.5" stroke="#1c1c1d" stroke-width=".9" fill="none"/></svg>
      </li>
    </ul>

    <address class="address">
      12345, Address Goes Here<br>
      Country Name, 123456.
    </address>
  </section>
</body>
</html>
```